A clean crisp business card for a Landscape Construction company. Designed to be easy to read contact/ info and also be appealing/interesting, unlike a traditional business card.

Industry/Entity Type

Landscape Construction

Contact Information for Business Card

Company name : Bramblecrest Landscape Construction, phone number: (877) 62Vales, website:Bramblecrestlandscapes.example, Email, sales@bramblecrestlandscapes.example

Requirements
Nice to have
• Luxurious finishes/ details…. Icons or emblems next to contact info
Should not have
• Clipart or general pictures

```html
<!DOCTYPE html>
<html lang="en">
<head>
<meta charset="utf-8">
<title>Bramblecrest Landscape Construction – Business Card</title>
<link rel="stylesheet" href="https://fonts.googleapis.com/css2?family=Cinzel:wght@600&family=Open+Sans:wght@400;600&display=swap">
<style>
  :root {
    --bg: #c9c9c9;
    --card: #ffffff;
    --blue: #2a6cc4;
    --green: #8cc63f;
    --ink: #2b2b2b;
    --shadow: rgba(0,0,0,0.22);
  }
  * { box-sizing: border-box; margin: 0; padding: 0; }
  html, body { width: 1200px; height: 675px; overflow: hidden; }
  body {
    background: var(--bg);
    display: flex;
    align-items: center;
    justify-content: center;
    gap: 60px;
    font-family: "Open Sans", Arial, sans-serif;
  }
  .card {
    position: relative;
    width: 520px;
    height: 297px;
    background: var(--card);
    border-radius: 16px;
    box-shadow: 0 10px 24px var(--shadow);
    overflow: hidden;
  }
  .wordmark {
    font-family: "Cinzel", "Times New Roman", serif;
    font-weight: 600;
    color: var(--blue);
    line-height: 1.15;
  }
  .wordmark .sub { display: block; font-size: 0.5em; letter-spacing: 0.22em; }

  /* Front */
  .card--front { display: flex; align-items: center; justify-content: center; }
  .card--front .wordmark { font-size: 34px; text-align: center; }

  /* Back */
  .card--back .wordmark {
    position: absolute; left: 46px; top: 52px; font-size: 30px;
  }
  .rule { position: absolute; left: 30px; height: 2px; width: 360px; }
  .rule--green { top: 150px; background: var(--green); }
  .rule--blue { top: 156px; background: var(--blue); }
  .contact-list {
    position: absolute; left: 30px; top: 178px; list-style: none;
    font-size: 13.5px; color: var(--ink);
  }
  .contact-list li { display: flex; align-items: center; gap: 9px; margin-bottom: 7px; }
  .contact-icon { width: 16px; height: 16px; flex: none; }
  .person {
    position: absolute; right: 34px; top: 150px; text-align: right;
  }
  .person-name {
    font-family: "Cinzel", "Times New Roman", serif; font-weight: 600;
    color: var(--blue); font-size: 22px; line-height: 1;
  }
  .person-role {
    font-size: 12px; color: var(--ink);
    border-bottom: 2px solid var(--blue); padding: 2px 0 2px 30px;
  }
</style>
</head>
<body>
  <section class="card card--back" aria-label="Business card, contact side">
    <div class="wordmark">Bramblecrest<span class="sub">Landscape Construction</span></div>
    <div class="rule rule--green"></div>
    <div class="rule rule--blue"></div>
    <ul class="contact-list">
      <li>
        <svg class="contact-icon" viewBox="0 0 16 16" aria-hidden="true"><circle cx="8" cy="8" r="8" fill="var(--green)"/><path d="M5.5 4.5l1.5 1.6-.8 1.1a5 5 0 0 0 2.6 2.6l1.1-.8 1.6 1.5-.9 1.1c-3 0-5.9-2.9-5.9-5.9z" fill="#fff"/></svg>
        (877) 62Vales
      </li>
      <li>
        <svg class="contact-icon" viewBox="0 0 16 16" aria-hidden="true"><circle cx="8" cy="8" r="8" fill="var(--green)"/><rect x="4" y="5.2" width="8" height="5.6" fill="#fff"/><path d="M4 5.2l4 3 4-3" stroke="var(--green)" stroke-width="1" fill="none"/></svg>
        www.bramblecrestlandscapes.example
      </li>
      <li>
        <svg class="contact-icon" viewBox="0 0 16 16" aria-hidden="true"><circle cx="8" cy="8" r="8" fill="var(--green)"/><circle cx="8" cy="8" r="4.2" fill="none" stroke="#fff" stroke-width="1"/><path d="M3.8 8h8.4M8 3.8c-2 2.6-2 5.8 0 8.4M8 3.8c2 2.6 2 5.8 0 8.4" stroke="#fff" stroke-width="0.9" fill="none"/></svg>
        sales@bramblecrestlandscapes.example
      </li>
    </ul>
    <div class="person">
      <div class="person-name">Name</div>
      <div class="person-role">Owner</div>
    </div>
  </section>

  <section class="card card--front" aria-label="Business card, logo side">
    <div class="wordmark">Bramblecrest<span class="sub">Landscape Construction</span></div>
  </section>
</body>
</html>
```